I need a new business card designed I have uploaded a picture of my current one so you can see what I use now.

I have a equipment and party rental business I want the card to be about the equipment rental side. If I chose your design I will then have you design a card for the party rental side of the business that I will get printed on the reverse of the first one.
I uploaded my logo which you can use.Mywebsite is kvhire-demo.net which you can look at for ideas. I am ok with darker colors for the equipment side like it currently is but open to colors. The party side should have colors and grab your attention.

```html
<!DOCTYPE html>
<html lang="en">
<head>
<meta charset="utf-8">
<title>Kestrel Valley Rental – Business Card</title>
<link href="https://fonts.googleapis.com/css2?family=Source+Sans+3:wght@400;600;700&display=swap" rel="stylesheet">
<style>
  :root {
    --backdrop: #e3e3e3;
    --card: #000000;
    --ink: #ffffff;
    --shadow: rgba(0,0,0,0.35);
  }
  * { margin: 0; padding: 0; box-sizing: border-box; }
  html, body { width: 848px; height: 1200px; overflow: hidden; }
  body {
    background: var(--backdrop);
    font-family: "Source Sans 3", "Myriad Pro", Arial, sans-serif;
    color: var(--ink);
    position: relative;
  }
  .card {
    position: absolute;
    left: 109px;
    width: 630px;
    height: 358px;
    background: var(--card);
    box-shadow: 6px 7px 8px var(--shadow);
  }
  .card--front { top: 219px; }
  .card--back { top: 621px; height: 359px; }

  .brand-name {
    position: absolute;
    text-align: center;
    font-weight: 700;
    color: var(--ink);
    line-height: 1.05;
    letter-spacing: 0.5px;
  }
  .card--front .brand-name {
    left: 215px; width: 200px; top: 70px; font-size: 24px;
  }
  .card--back .brand-name {
    left: 66px; width: 240px; top: 148px; font-size: 28px;
  }

  .identity {
    position: absolute;
    right: 324px;
    top: 200px;
    text-align: right;
  }
  .identity__name { font-size: 27px; font-weight: 700; line-height: 1; }
  .identity__role { font-size: 18px; margin-top: 6px; line-height: 1; }
  .identity__rule {
    width: 16px; height: 1.5px; background: var(--ink);
    margin: 6px 0 8px auto;
  }
  .identity__address { font-size: 18px; line-height: 21px; }

  .divider {
    position: absolute;
    width: 1.5px;
    background: var(--ink);
  }
  .card--front .divider { left: 311px; top: 205px; height: 92px; }
  .card--back .divider { left: 333px; top: 100px; height: 162px; }

  .contact-list {
    position: absolute;
    left: 347px;
    top: 205px;
    list-style: none;
  }
  .contact-list li {
    display: flex;
    align-items: center;
    height: 30px;
    font-size: 18px;
  }
  .contact-list svg { width: 18px; height: 18px; margin-right: 10px; fill: var(--ink); }

  .site-link {
    position: absolute;
    left: 0; right: 0;
    top: 318px;
    text-align: center;
    font-size: 18px;
    font-weight: 700;
  }

  .service-list {
    position: absolute;
    left: 353px;
    top: 100px;
    list-style: none;
  }
  .service-list li {
    font-size: 18.5px;
    height: 27.5px;
    line-height: 27.5px;
    padding-left: 19px;
    position: relative;
  }
  .service-list li::before {
    content: "";
    position: absolute;
    left: 0; top: 10px;
    width: 9px; height: 9px;
    border-radius: 50%;
    background: var(--ink);
  }
</style>
</head>
<body>

<section class="card card--front">
  <div class="brand-name">Kestrel Valley<br>Rental</div>

  <div class="identity">
    <div class="identity__name">Dana Whitlock</div>
    <div class="identity__role">Founder</div>
    <div class="identity__rule"></div>
    <div class="identity__address">48 Orchard Lane<br>Millbrook NY 10000</div>
  </div>

  <div class="divider"></div>

  <ul class="contact-list">
    <li>
      <svg viewBox="0 0 24 24" aria-hidden="true"><path d="M6.6 10.8a15.1 15.1 0 0 0 6.6 6.6l2.2-2.2c.3-.3.7-.4 1-.2 1.1.4 2.3.6 3.6.6.6 0 1 .4 1 1V20c0 .6-.4 1-1 1A17 17 0 0 1 3 4c0-.6.4-1 1-1h3.5c.6 0 1 .4 1 1 0 1.3.2 2.5.6 3.6.1.3 0 .7-.2 1z"/></svg>
      (555)014-2297
    </li>
    <li>
      <svg viewBox="0 0 24 24" aria-hidden="true"><path d="M6 2h10l2 2v4H6zM4 9h16a2 2 0 0 1 2 2v6h-4v5H6v-5H2v-6a2 2 0 0 1 2-2zm4 6v5h8v-5z"/></svg>
      Fax (555)014-2298
    </li>
    <li>
      <svg viewBox="0 0 24 24" aria-hidden="true"><path d="M12 2a10 10 0 1 0 0 20 10 10 0 0 0 0-20zm-1 17.9A8 8 0 0 1 4.1 11H7c0 3.5 1.5 6.6 4 8.9zM7 9H4.3A8 8 0 0 1 11 4.1C9 6 7.4 7.5 7 9zm6 10.9V13h6.9A8 8 0 0 1 13 19.9zM13 11V4.1A8 8 0 0 1 19.9 11z"/></svg>
      www.kvhire-demo.net
    </li>
  </ul>

  <div class="site-link">KestrelValleyEquipment-demo.net</div>
</section>

<section class="card card--back">
  <div class="brand-name">Kestrel Valley<br>Rental</div>

  <div class="divider"></div>

  <ul class="service-list">
    <li>Excavator &amp; Loaders</li>
    <li>Lifts &amp; Pumps</li>
    <li>Tillers &amp; Power Tools</li>
    <li>Tables &amp; Chairs</li>
    <li>Bounce Houses</li>
    <li>Canopies</li>
  </ul>
</section>

</body>
</html>
```